Web Design Project

We need a web design for a new business in Orland Park, IL.
We are a restaurant meal delivery business. We deliver from a variety of restaurants. We gives our customers an alternative to just pizza delivery.

Websites we like:
http://www.brambleporter.example/
https://www.quillfetchgo.example/Default.asp
www.wendlerunner.example/

Our current website is www.tovenbasket.example(not to be used as a guide, i'm looking for an original design)
Updates

Please no pictures of anything associated with Pizza.  We are a restaurant delivery business that gives our customers an alternative to just pizza delivery. 

This is my original logo.  I uploaded the file to the job brief and updated the brief some.

Target Market(s)

Two income households with children.

Industry/Entity Type

Business

Requirements
Must have
• Order Now button,and sliding photographs of food.
Nice to have
• a background other than white(it can be white if it works with the design)
Should not have
• A picture of pizza that cant be changed. It is ok if the photo is apart of sliding photo's, but pizza cant be the main focus of our delivery service.

```html
<!DOCTYPE html>
<html lang="en">
<head>
<meta charset="utf-8">
<title>Toven Basket – Restaurant Meal Delivery</title>
<link rel="stylesheet" href="https://fonts.googleapis.com/css2?family=Roboto+Condensed:wght@400;700&family=Signika:wght@300;400&display=swap">
<style>
:root{
  --red:#a80000;
  --red-dark:#7d0000;
  --red-deep:#5c0606;
  --red-night:#3b0202;
  --grey-bg:#ebebeb;
  --pink-top:#efd6d0;
  --text:#4a4a4a;
  --muted:#8a8a8a;
  --white:#ffffff;
  --green:#8db66a;
}
*{margin:0;padding:0;box-sizing:border-box}
html,body{width:1061px;height:1200px;overflow:hidden}
body{position:relative;background:var(--white);font-family:"Signika",sans-serif;font-weight:300;color:var(--text)}
.head-font{font-family:"Roboto Condensed",sans-serif}
.wrap{position:absolute;left:139px;width:784px}

/* header */
.site-header{position:absolute;top:0;left:0;width:1061px;height:108px}
.brand{position:absolute;left:139px;top:30px;display:flex;align-items:center;gap:6px;font-family:"Roboto Condensed",sans-serif;font-weight:700;font-size:26px;color:var(--red)}
.brand-dot{width:14px;height:14px;border-radius:50%;background:var(--red)}
.phone{position:absolute;right:139px;top:20px;display:flex;align-items:center;gap:6px;font-family:"Roboto Condensed",sans-serif;font-size:15px;color:var(--red)}
.header-btn{position:absolute;top:56px;width:135px;height:33px;background:var(--red);border-radius:4px;color:var(--white);display:flex;align-items:center;gap:10px;padding-left:10px;font-family:"Roboto Condensed",sans-serif;font-size:15px}
.header-btn .ico{width:30px;height:20px;background:#e9e9e9;border-radius:2px}
.btn-order{left:632px}.btn-account{left:787px}

/* nav */
.main-nav{position:absolute;top:108px;left:0;width:1061px;height:63px;background:var(--red)}
.main-nav ul{list-style:none;position:absolute;left:139px;top:0;display:flex;align-items:center;height:63px}
.main-nav li{font-family:"Roboto Condensed",sans-serif;font-size:14px;color:var(--white);display:flex;align-items:center}
.main-nav li+li::before{content:"|";margin:0 11px}
.main-nav li.home+li::before{content:"";margin:0 7px}
.main-nav li.home{background:var(--white);color:var(--red);height:49px;margin-top:0;padding:21px 14px 0;border-radius:0 0 4px 4px;align-self:flex-start;height:49px}

/* hero */
.hero{position:absolute;top:171px;left:0;width:1061px;height:325px;background:var(--grey-bg)}
.hero-frame{position:absolute;left:139px;top:15px;width:493px;height:294px;background:var(--white);border:1px solid #d6d6d6;padding:6px;box-shadow:0 6px 8px -6px rgba(0,0,0,.25)}
.hero-photo{width:100%;height:100%;background:linear-gradient(135deg,#f2e3c8 0%,#8a3a2a 35%,#6d2a1c 55%,#d7412a 75%,#f1c47a 100%)}
.welcome{position:absolute;left:648px;top:12px;width:268px}
.welcome h1{font-family:"Roboto Condensed",sans-serif;font-weight:400;font-size:20px;color:var(--red);margin-bottom:12px}
.welcome p{font-size:10.2px;line-height:16.3px;text-align:justify;padding-left:3px}
.more{font-size:10.5px;color:#555;display:flex;align-items:center;gap:3px;justify-content:flex-end}
.more::after{content:"";width:7px;height:7px;border-top:2px solid var(--red);border-right:2px solid var(--red);transform:rotate(45deg);margin-left:1px}
.welcome .more{margin-top:8px}
.order-banner{position:absolute;left:632px;top:253px;width:291px;height:44px}
.order-banner span{position:absolute;left:56px;top:11px;font-family:"Roboto Condensed",sans-serif;font-size:17px;color:var(--white)}
.order-banner .box{position:absolute;left:18px;top:6px;width:30px;height:30px;background:#f0c478;border-radius:2px}

/* features */
.features{position:absolute;top:496px;left:0;width:1061px;height:437px;background:linear-gradient(180deg,var(--pink-top) 0%,#f2e6e4 40%,#ececec 100%)}
.card{position:absolute;top:20px;width:245px;height:149px;background:var(--white);box-shadow:0 8px 8px -8px rgba(0,0,0,.3);padding:10px}
.card .photo{position:absolute;left:10px;top:10px;width:111px;height:129px}
.card h2{position:absolute;left:130px;top:14px;font-family:"Roboto Condensed",sans-serif;font-weight:400;font-size:16.5px;color:var(--red)}
.card p{position:absolute;left:132px;top:42px;width:106px;font-size:10px;line-height:14.7px}
.card .more{position:absolute;right:14px;bottom:12px}
.c1{left:139px}.c2{left:408px}.c3{left:677px}

.online{position:absolute;left:139px;top:182px;width:514px}
.sec-title{display:flex;align-items:center;gap:6px;font-family:"Roboto Condensed",sans-serif;font-size:17px;color:var(--red)}
.sec-icon{width:42px;height:42px;border-radius:50%;background:#c41a1a}
.online p{margin-top:8px;padding-left:8px;font-size:10.2px;line-height:16.3px;text-align:justify;position:relative}
.online p::before{content:"\201C";position:absolute;left:-1px;top:-5px;font-size:16px;font-weight:400}
.online p::after{content:"\201D";font-size:14px;font-weight:400;margin-left:4px}

.search-bar{position:absolute;left:139px;top:349px;width:514px;height:62px;background:var(--red);border-radius:5px;overflow:hidden}
.search-bar .label{position:absolute;left:0;top:0;width:110px;height:62px;background:#5e0202;color:var(--white);font-family:"Roboto Condensed",sans-serif;font-size:14px;line-height:15.5px;text-align:center;padding-top:15px}
.field{position:absolute;top:16px;height:29px;background:var(--white);border-radius:3px;font-size:10px;color:#999;padding:9px 12px}
.f-select{left:129px;width:114px}
.f-drop{position:absolute;left:243px;top:16px;width:27px;height:29px;background:#5e0202;border-radius:0 3px 3px 0}
.f-text{left:287px;width:141px}
.search-btn{position:absolute;left:439px;top:16px;width:64px;height:29px;background:#5e0202;border-radius:3px;color:var(--white);font-family:"Roboto Condensed",sans-serif;font-size:12px;text-align:center;line-height:29px}

.certs{position:absolute;left:677px;top:182px;width:245px}
.cert-badge{width:48px;height:38px;background:#cfd9e8;border-radius:4px}
.cert-card{position:absolute;top:54px;left:0;width:245px;height:171px;border-radius:5px;overflow:hidden;background:var(--green)}
.cert-copy{position:absolute;left:0;top:0;width:151px;text-align:center;color:#1d2a12}
.cert-copy .small{font-size:9.6px;margin-top:28px;font-weight:400}
.cert-copy .big{font-family:"Roboto Condensed",sans-serif;font-weight:700;color:var(--white);font-size:44px;line-height:40px;margin-top:4px}
.cert-copy .pct{font-size:44px}
.cert-copy .fine{font-size:9.6px;line-height:12px;font-weight:400}
.cert-photo{position:absolute;right:0;top:0;width:94px;height:171px;background:linear-gradient(160deg,#caa66a 0%,#f3efe6 40%,#d44a22 70%,#f1d28a 100%)}

/* footer */
.site-footer{position:absolute;top:933px;left:0;width:1061px;height:209px;background:var(--red-deep)}
.fcol{position:absolute;top:18px}
.fcol h3{font-family:"Roboto Condensed",sans-serif;font-weight:400;font-size:16.5px;color:var(--white);margin-bottom:10px}
.fcol p,.fcol li{font-size:10px;color:#b36a6a;line-height:14.7px}
.menu{list-style:none;width:146px}
.menu li{border-bottom:1px solid #3d0303;line-height:20.5px;padding-top:1px}
.menu li:last-child{border:none}
.fc1{left:140px}.fc2{left:317px;width:176px}.fc3{left:532px;width:180px}.fc4{left:742px;width:180px}
.fcol .url{color:var(--white)}
.tweet-meta{display:flex;align-items:center;gap:10px;color:var(--white);font-weight:400;font-size:10.5px;margin:8px 0 10px 2px}
.tweet-meta i{width:18px;height:12px;border-radius:50%;background:#d81d1d;display:block}
.foot-btn{position:absolute;width:64px;height:25px;background:#cc0000;border-radius:3px;color:var(--white);font-family:"Roboto Condensed",sans-serif;font-size:12px;text-align:center;line-height:25px}
.qf{height:23px;background:#efefef;border-radius:3px;margin-bottom:5px;font-size:10px;color:#888;padding:5px 14px}
.qf.area{height:54px}
.bottom-bar{position:absolute;top:1142px;left:0;width:1061px;height:58px;background:var(--red-night)}
.copy{position:absolute;left:143px;top:22px;font-size:10px;color:#6a0c0c}
.social{position:absolute;right:139px;top:17px;display:flex;gap:8px}
.social span{width:25px;height:25px;border-radius:3px;display:block}
</style>
</head>
<body>

<header class="site-header">
  <div class="brand"><span class="brand-dot"></span>Toven Basket</div>
  <div class="phone">
    <svg width="24" height="22" viewBox="0 0 24 22" aria-hidden="true"><circle cx="13" cy="11" r="9.5" fill="none" stroke="#a80000" stroke-width="1.5"/><path d="M3 5c-2 4 0 10 5 13l2-3-3-2 1-3-3-1z" fill="#a80000"/></svg>
    0777-5530-21
  </div>
  <a class="header-btn btn-order"><span class="ico"></span>Order Now</a>
  <a class="header-btn btn-account"><span class="ico"></span>My Account</a>
</header>

<nav class="main-nav">
  <ul>
    <li class="home">Home</li>
    <li>About Us</li>
    <li>Corporate</li>
    <li>How Do I Order?</li>
    <li>Restaurants</li>
    <li>Gift Certificate</li>
    <li>Comments</li>
    <li>Contact Us</li>
  </ul>
</nav>

<section class="hero">
  <div class="hero-frame"><div class="hero-photo" role="img" aria-label="Sliced seared duck breast with roasted cherry tomatoes, herbs and mashed potato"></div></div>
  <div class="welcome">
    <h1>Welcome to Toven Basket</h1>
    <p>Lorem Ipsum is simply dummy text of the printing and typesetting industry. Lorem Ipsum has been the industry's standard dummy text ever since the 1500s, when an unknown printer took a galley of type and scrambled it to make a type specimen book. It has survived not only five centuries, but also the leap into electronic typesetting, remaining essentially unchanged. It was popularised in the 1960s with the release of Lettermark sheets containing Lorem Ipsum passages, and more recently with desktop publishing software like Folio Layout including ver-</p>
    <div class="more">More</div>
  </div>
  <div class="order-banner">
    <svg width="291" height="44" viewBox="0 0 291 44" aria-hidden="true" style="position:absolute;left:0;top:0"><path d="M0 0H269L248 22L291 44H0Z" fill="#a80000"/><path d="M269 0L291 0L291 44L248 22Z" fill="#ebebeb"/></svg>
    <div class="box"></div>
    <span>Order Meals Delivery Now</span>
  </div>
</section>

<section class="features">
  <article class="card c1">
    <div class="photo" role="img" aria-label="Bowl of noodle soup with vegetables" style="background:linear-gradient(135deg,#e9dcc2,#d9b26a 60%,#8a9c48)"></div>
    <h2>Our Lunch</h2>
    <p>Lorem Ipsum is simply dummy text the printing and typesetting industry. Lorem Ipsum has</p>
    <div class="more">More</div>
  </article>
  <article class="card c2">
    <div class="photo" role="img" aria-label="Grilled salmon fillets with green beans and lemon" style="background:linear-gradient(135deg,#eef0ee,#e98a55 50%,#5f8a3a)"></div>
    <h2>Our Specials</h2>
    <p>Lorem Ipsum is simply dummy text the printing and typesetting industry. Lorem Ipsum has</p>
    <div class="more">More</div>
  </article>
  <article class="card c3">
    <div class="photo" role="img" aria-label="Roast chicken with a bottle of white wine and glasses" style="background:linear-gradient(135deg,#f5d84a,#e8a92a 55%,#9a5a20)"></div>
    <h2>Our Services</h2>
    <p>Lorem Ipsum is simply dummy text the printing and typesetting industry. Lorem Ipsum has</p>
    <div class="more">More</div>
  </article>

  <div class="online">
    <div class="sec-title"><span class="sec-icon" role="img" aria-label="Cooking pot icon"></span>Online Food Delivery Available</div>
    <p>Lorem Ipsum is simply dummy text of the printing and typesetting industry. Lorem Ipsum has been the industry's standard dummy text ever since the 1500s, when an unknown printer took a galley of type and scrambled it to make a type specimen book. It has survived not only five centuries, but also the leap into electronic typesetting, remaining essentially unchanged. It was popularised in the 1960s with the release of Lettermark sheets containing Lorem Ipsum passages, and more recently with desktop publishing software like Folio Layout including versions of Lorem Ipsum.</p>
  </div>

  <form class="search-bar">
    <div class="label">Order Meal<br>Delivery Now</div>
    <div class="field f-select">Select Your ZIP Code</div>
    <div class="f-drop"><svg width="27" height="29" viewBox="0 0 27 29" aria-hidden="true"><path d="M8 12l5.5 5.5L19 12" fill="none" stroke="#fff" stroke-width="1.5"/></svg></div>
    <div class="field f-text">SearchYour ZIP Code</div>
    <div class="search-btn">Search</div>
  </form>

  <div class="certs">
    <div class="sec-title"><span class="cert-badge"></span>&nbsp;Get Certificates</div>
    <div class="cert-card">
      <div class="cert-copy">
        <div class="small">Tasty Savings, Just for You!</div>
        <div class="big">SAVE<br><span class="pct">80</span><sup style="font-size:18px">%</sup></div>
        <div class="fine">Get <b>$25</b> Restaurant<br>Gift Certificates for only <b>$2</b></div>
      </div>
      <div class="cert-photo" role="img" aria-label="Plate of spaghetti with tomato sauce and bread"></div>
    </div>
  </div>
</section>

<footer class="site-footer">
  <div class="fcol fc1">
    <h3>More Menu</h3>
    <ul class="menu">
      <li>About Us</li><li>Corporate</li><li>How Do I Order?</li><li>Corporate Account Signup</li><li>FAQ</li><li>Site Map</li><li>Contact Us</li>
    </ul>
  </div>
  <div class="fcol fc2">
    <h3>Whats is New</h3>
    <p>Lorem Ipsum is simply dummy text of the printing and typesetting industry. Lorem Ipsum has been the industry's standard dummy text ever since the 1500s, when an unknown printer took a galley of type and scrambled it to make a type specimen book. It has survived not only five centuries, but</p>
    <div class="foot-btn" style="left:113px;top:169px">More</div>
  </div>
  <div class="fcol fc3">
    <h3>Recent Tweets</h3>
    <p>Lorem Ipsum is simply dummy<br><span class="url">http:// typeset .example</span>. Lorem Ipsum has been the industry's standard dum</p>
    <div class="tweet-meta"><i></i>20 days ago</div>
    <p>Lorem Ipsum is simply dummy<br><span class="url">http:// typeset .example</span>. Lorem Ipsum has been the industry's standard dum</p>
    <div class="tweet-meta"><i></i>20 days ago</div>
  </div>
  <div class="fcol fc4">
    <h3>Quick Contact</h3>
    <div class="qf">Name*</div>
    <div class="qf">Email*</div>
    <div class="qf area">Comment*</div>
    <div class="foot-btn" style="left:115px;top:169px">Submit</div>
  </div>
</footer>

<div class="bottom-bar">
  <div class="copy">2012 © - Toven Basket. All Rights Reserved</div>
  <div class="social">
    <span style="background:#1f7fb8" role="img" aria-label="Professional network link"></span>
    <span style="background:#f08a1c" role="img" aria-label="News feed link"></span>
    <span style="background:#3e6487" role="img" aria-label="Blog link"></span>
    <span style="background:#3c5a98" role="img" aria-label="Social profile link"></span>
  </div>
</div>

</body>
</html>
```